PSD for Magento Site (No Code Required)

I Need 10 pages design for a new Plus-Size Lingerie Site. The site has to be a edgy, fun & clean.

I will need versions of each page for mobile, tablet sizes as well. We are trying to be a new kind of lingerie site. something non traditional. A Fun place to show. Big images, Easy Navigation, Simple Layout.

Full Brief is Attached.

Target Market(s)

Plus size Women, Lingerie Enthusiasts

Industry/Entity Type

Retail

Number of Pages Required

5+ page

Font styles to use
Sans Serif

Colors
000000
ffffff
d3d3d3

Requirements
Must have
• Well Structured Mobile versions of each page
Should not have
• clutter

```html
<!DOCTYPE html>
<html lang="en">
<head>
<meta charset="utf-8">
<title>Plumline — Plus Size Lingerie Store</title>
<link rel="stylesheet" href="https://fonts.googleapis.com/css2?family=Oswald:wght@400;500;600&family=Open+Sans:wght@400;600;700&display=swap">
<style>
:root{
  --ink:#222;
  --header:#1e1e1e;
  --footer:#3a3a3a;
  --footer-base:#262626;
  --accent:#f7941d;
  --grey:#d3d3d3;
  --muted:#8a8a8a;
  --line:#e4e4e4;
  --page:#f4f4f4;
  --white:#fff;
}
*{box-sizing:border-box;margin:0;padding:0}
html,body{width:1200px;height:3214px;overflow:hidden}
body{font-family:"Open Sans",Arial,sans-serif;color:var(--ink);background:var(--page);font-size:12px}
ul{list-style:none}
.wrap{width:1028px;margin:0 auto;position:relative}

/* top bar */
.topbar{height:71px;background:var(--header);color:var(--white)}
.topbar .wrap{display:flex;align-items:center;height:71px}
.logo{display:flex;flex-direction:column;width:220px}
.logo-name{font-family:"Oswald",sans-serif;font-weight:500;font-size:28px;letter-spacing:1px;line-height:1;color:var(--white)}
.logo-sub{font-size:9px;letter-spacing:9px;color:var(--grey);margin-top:4px}
.store-switch{display:flex;height:71px;margin-left:80px}
.store-switch a{display:flex;align-items:center;padding:0 14px;font-size:11px;color:var(--white);text-decoration:none}
.store-switch .active{background:#4a4a4a}
.top-search{margin-left:24px;width:320px;height:34px;border-radius:17px;background:#444;display:flex;align-items:center;justify-content:space-between;padding:0 16px;font-size:11px;color:#bbb}
.top-links{margin-left:auto;display:flex;gap:32px;font-size:11px}
.top-links span{display:flex;align-items:center;gap:6px}

/* nav */
.mainnav{height:57px;background:var(--white);border-bottom:1px solid var(--line)}
.mainnav ul{display:flex;height:57px;align-items:center;gap:34px;font-size:11px;color:#444}
.mainnav li::after{content:"";display:inline-block}
.mainnav .dd::after{content:" \25BE";font-size:9px}

/* hero */
.hero{height:467px;position:relative;background:linear-gradient(100deg,#6b5440 0%,#b59a80 35%,#8a7058 60%,#3c2e24 100%)}
.hero-text{position:absolute;right:86px;top:200px;text-align:right;color:var(--white)}
.hero-title{font-family:"Oswald",sans-serif;font-weight:600;font-size:46px;color:var(--accent);letter-spacing:1px;line-height:1}
.hero-sub{font-family:"Oswald",sans-serif;font-size:24px;letter-spacing:4px;color:#ddd;margin-top:8px}
.hero-copy{font-size:11px;line-height:26px;margin-top:14px;width:380px;margin-left:auto}
.hero-off{font-family:"Oswald",sans-serif;font-size:48px;margin-top:10px;line-height:1}
.hero-off b{color:var(--accent);font-weight:600}
.hero-off small{font-size:24px;color:var(--accent)}
.hero-dots{position:absolute;left:86px;bottom:14px;display:flex;gap:6px}
.hero-dots i{width:14px;height:14px;border-radius:50%;border:2px solid var(--white)}
.hero-dots i.on{background:var(--white)}

/* collections */
.collections{display:flex;gap:19px;margin-top:18px}
.collection{width:330px;height:270px;position:relative;display:flex;flex-direction:column;align-items:center;justify-content:center;color:var(--white);border:4px solid #222}
.collection.c1{background:linear-gradient(160deg,#8ea3b4,#6b5a48 60%,#3e3428)}
.collection.c2{background:linear-gradient(160deg,#2a2430,#5a4a52 55%,#1d1a1e)}
.collection.c3{background:linear-gradient(160deg,#a9a59c,#7d6c5c 55%,#4a3d32)}
.collection h3{font-family:"Oswald",sans-serif;font-weight:600;font-size:56px;line-height:1;margin-top:70px}
.collection p{font-family:"Oswald",sans-serif;font-size:24px;letter-spacing:7px;line-height:1.1}
.btn{display:inline-block;background:var(--accent);color:var(--white);font-size:11px;text-transform:uppercase}
.collection .btn{padding:6px 18px;margin-top:10px}

/* catalog */
.catalog{display:flex;gap:30px;margin-top:30px}
.sidebar{width:208px}
.filter{margin-bottom:28px}
.filter h4{font-size:12px;font-weight:700;display:flex;justify-content:space-between;padding-bottom:8px;border-bottom:2px solid var(--line);margin-bottom:10px;position:relative}
.filter h4::after{content:"";position:absolute;left:0;bottom:-2px;width:60px;height:2px;background:var(--accent)}
.filter h4 .ico{width:12px;height:12px;border:2px solid #888;border-radius:2px}
.search-box{display:flex;justify-content:space-between;align-items:center;border:1px solid var(--line);background:var(--white);height:30px;padding:0 10px;font-size:10px;color:#aaa}
.cat-list li{font-size:10px;color:#555;height:24px;display:flex;align-items:center;gap:8px}
.cat-list li::before{content:"\00BB";color:#999}
.check-list{border-right:4px solid var(--grey)}
.check-list li{font-size:10px;color:#555;height:24px;display:flex;align-items:center;gap:10px}
.check-list li::before{content:"";width:10px;height:10px;border:1px solid #bbb;background:var(--white)}
.swatches{display:grid;grid-template-columns:repeat(8,20px);gap:6px}
.swatches i{width:20px;height:20px;border:1px solid #ccc;display:block}
.main{width:790px}
.section-title{font-family:"Oswald",sans-serif;font-weight:500;font-size:18px;padding-bottom:10px;border-bottom:1px solid var(--line);margin-bottom:22px;position:relative}
.grid{display:grid;grid-template-columns:repeat(3,255px);gap:22px 12px;margin-bottom:32px}
.card{background:var(--white);height:418px}
.card-photo{height:313px;position:relative}
.card-photo .sizes{position:absolute;left:60px;bottom:4px;background:#eee;border:1px solid #999;font-size:10px;padding:2px 8px}
.card-body{padding:10px 10px}
.card-row{display:flex;justify-content:space-between;align-items:center}
.card-name{font-size:12px;text-transform:uppercase;color:#333}
.stars{color:var(--accent);font-size:10px;letter-spacing:1px}
.price{color:var(--accent);font-size:13px;margin-top:6px}
.price-row{display:flex;align-items:center;gap:8px;margin-top:6px}
.price-row .price{margin-top:0}
.dots{display:flex;gap:3px;font-size:9px;color:#888;align-items:center}
.dots i{width:10px;height:10px;border-radius:50%;display:block}
.actions{display:flex;gap:4px;margin-top:10px}
.actions span{height:26px;border:1px solid var(--line);display:flex;align-items:center;justify-content:center;font-size:9px;color:#555;min-width:28px}
.actions .add{padding:0 12px;gap:6px}
.p1{background:linear-gradient(160deg,#cfcfcf,#5a5f7a 60%,#2d2f48)}
.p2{background:linear-gradient(160deg,#5f7a4a,#3e5a34 55%,#c4ab94)}
.p3{background:linear-gradient(160deg,#6a5848,#3a3430 50%,#b49e8a)}
.p4{background:linear-gradient(160deg,#3e5a3a,#0f6f82 55%,#1d3e46)}
.p5{background:linear-gradient(160deg,#d0c8c0,#c8302c 55%,#8e7060)}
.p6{background:linear-gradient(160deg,#ececec,#2a2a2a 55%,#c8b8a8)}
.p7{background:linear-gradient(160deg,#e8e8e8,#2a2a2a 50%,#c9b2a0)}
.p8{background:linear-gradient(160deg,#5f7040,#7a2a55 55%,#b89a88)}
.p9{background:linear-gradient(160deg,#6b8058,#2a2a2a 55%,#cdb6a2)}
.p10{background:linear-gradient(160deg,#8fb0c0,#d62a34 55%,#6e8a9c)}
.p11{background:linear-gradient(160deg,#c8ccc8,#2a2826 55%,#bfae9e)}
.p12{background:linear-gradient(160deg,#d8d8d8,#e3b6ae 50%,#2a2a2a)}
.pager{display:flex;justify-content:flex-end;gap:14px;font-size:12px;font-weight:700;margin-top:-6px}
.pager .cur{color:#d62a34;border-bottom:2px solid #d62a34}

/* promo */
.promo{position:absolute;left:0;top:2857px;width:1200px;height:89px;background:var(--white)}
.promo .wrap{display:flex;justify-content:space-between;align-items:center;height:89px}
.promo h2{font-family:"Oswald",sans-serif;font-weight:400;font-size:26px}
.promo h2 b{color:var(--accent);font-weight:400}
.promo p{font-size:10px;color:var(--muted);margin-top:4px}
.promo .btn{padding:12px 36px;font-size:13px}

/* footer */
.footer{position:absolute;left:0;top:2946px;width:1200px;height:204px;background:var(--footer);color:#ccc}
.footer .wrap{display:flex;padding-top:22px}
.f-col{font-size:10px}
.f-col h5{font-size:12px;color:var(--white);text-transform:uppercase;margin-bottom:14px;font-weight:700}
.f-col li{height:20px}
.f-col li::before{content:"\00BB  ";color:#999}
.f-brand{width:244px;font-size:10px;line-height:20px}
.f-brand .logo-name{font-size:28px}
.f-brand p{margin-top:10px;width:210px}
.f-news{width:210px}
.f-news input{width:180px;height:24px;border:0;background:#ddd;font-size:9px;padding:0 8px;margin-top:8px;font-family:inherit}
.f-news .btn{padding:4px 10px;margin-top:10px;font-size:9px}
.f-contact li{height:24px}
.f-contact li::before{content:""}
.f-contact b{color:var(--white)}
.base{position:absolute;left:0;top:3150px;width:1200px;height:64px;background:var(--footer-base);color:#ccc}
.base .wrap{display:flex;justify-content:space-between;align-items:center;height:64px;font-size:10px}
.social{display:flex;gap:8px}
.social i{width:30px;height:30px;border-radius:50%;background:var(--white);display:block}
</style>
</head>
<body>

<header class="topbar">
  <div class="wrap">
    <div class="logo"><span class="logo-name">PLUMLINE</span><span class="logo-sub">LINGERIE</span></div>
    <nav class="store-switch"><a href="#">STANDARD</a><a href="#" class="active">PLUS SIZE</a></nav>
    <div class="top-search">SEARCH
      <svg width="12" height="12" viewBox="0 0 12 12"><circle cx="5" cy="5" r="3.5" fill="none" stroke="#ddd" stroke-width="1.5"/><line x1="7.5" y1="7.5" x2="11" y2="11" stroke="#ddd" stroke-width="1.5"/></svg>
    </div>
    <div class="top-links">
      <span><svg width="10" height="10"><circle cx="5" cy="5" r="4.5" fill="#fff"/></svg>HELP</span>
      <span><svg width="10" height="10"><circle cx="5" cy="3" r="2.5" fill="#fff"/><rect x="1" y="6" width="8" height="4" rx="2" fill="#fff"/></svg>LOGIN</span>
      <span><svg width="12" height="10"><path d="M0 1h2l2 6h7l1-5H3" fill="none" stroke="#fff"/></svg>CART</span>
    </div>
  </div>
</header>

<nav class="mainnav">
  <div class="wrap">
    <ul>
      <li class="dd">LINGERIE</li><li>COSTUMES</li><li>PANTIES</li><li>DRESSES</li><li class="dd">SLEEPWEAR</li><li class="dd">HOSIERY</li><li class="dd">ACCESSORIES</li><li class="dd">PVC/LEATHER</li><li class="dd">HOLIDAY COLLECTION</li><li>SALE &amp; CLEARANCE</li>
    </ul>
  </div>
</nav>

<section class="hero" role="img" aria-label="Model in white lace lingerie lying on fur">
  <div class="hero-text">
    <div class="hero-title">PLUMLINE</div>
    <div class="hero-sub">PLUS SIZE LINGERIE STORE</div>
    <p class="hero-copy">IT IS A LONG ESTABLISHED FACT THAT A READER WILL BE DISTRACTED BY OF A PAGE WHEN LOOKING AT ITS LAYOUT</p>
    <div class="hero-off"><b>50<small>%</small></b> OFF</div>
  </div>
  <div class="hero-dots"><i></i><i></i><i class="on"></i><i></i><i></i></div>
</section>

<div class="wrap">
  <section class="collections">
    <div class="collection c1" role="img" aria-label="Summer collection photo of a model outdoors"><h3>SUMMER</h3><p>COLLECTIONS</p><span class="btn">Shop now</span></div>
    <div class="collection c2" role="img" aria-label="Sexy collection photo of a model at night"><h3>SEXY</h3><p>COLLECTIONS</p><span class="btn">Shop now</span></div>
    <div class="collection c3" role="img" aria-label="Newest collection photo of a model by a window"><h3>NEWEST</h3><p>COLLECTIONS</p><span class="btn">Shop now</span></div>
  </section>

  <div class="catalog">
    <aside class="sidebar">
      <div class="filter"><h4>SEARCH</h4><div class="search-box">Enter key word...<svg width="10" height="10"><circle cx="4" cy="4" r="3" fill="none" stroke="#999"/><line x1="6" y1="6" x2="9.5" y2="9.5" stroke="#999"/></svg></div></div>
      <div class="filter"><h4>CATEGORY <span class="ico"></span></h4>
        <ul class="cat-list"><li>LINGERIE</li><li>COSTUMES</li><li>PANTIES</li><li>DRESSES</li><li>SLEEPWEAR</li><li>HOSIERY</li><li>ACCESSORIES</li><li>PVC/LEATHER</li><li>HOLIDAY COLLECTION</li><li>SALE &amp; CLEARANCE</li></ul></div>
      <div class="filter"><h4>SIZE <span class="ico"></span></h4>
        <ul class="check-list"><li>32A (28)</li><li>32B (23)</li><li>32C (23)</li><li>32D (11)</li><li>32DD (13)</li><li>34A (25)</li></ul></div>
      <div class="filter"><h4>COLOR <span class="ico" style="border-radius:50%"></span></h4>
        <div class="swatches">
          <i style="background:#f4a15a"></i><i style="background:#f47f8a"></i><i style="background:#7a3fa0"></i><i style="background:#d63a3a"></i><i style="background:#7cb342"></i><i style="background:#f5c242"></i><i style="background:#6b3e1f"></i><i style="background:#fff"></i>
          <i style="background:#1e4da0"></i><i style="background:#1d8fbf"></i><i style="background:#1eb0a5"></i><i style="background:#fff"></i><i style="background:#111"></i><i style="background:#b0428d"></i><i style="background:#3a3a3a"></i><i style="background:#999"></i>
        </div></div>
      <div class="filter"><h4>PRICE <span>$</span></h4>
        <ul class="check-list"><li>RS. 249 AND BELOW</li><li>RS. 250 - RS. 499</li><li>RS. 500 - RS. 999</li><li>RS. 1000 - RS. 1499</li><li>RS. 1500 - RS. 1999</li><li>RS. 2000 AND ABOVE</li></ul></div>
      <div class="filter"><h4>BRAND <span class="ico"></span></h4>
        <ul class="check-list"><li>JOYLINE</li><li>VELVETTA</li><li>CORVINA</li><li>TESSA &amp; CO</li><li>LOVELLA</li><li>TRILLIUM</li></ul></div>
      <div class="filter"><h4>MATERIA <span class="ico"></span></h4>
        <ul class="check-list"><li>READER WILL BE</li><li>CONTRARY TO POPULAR</li><li>DISTRACTED</li><li>SIMPLY RANDOM</li><li>FINIBUS BONORUM</li></ul></div>
      <div class="filter"><h4>SORT BY <span class="ico"></span></h4>
        <ul class="check-list" style="border:0"><li>NEWEST ARRIVAL</li><li>TOP SELLERS</li><li>PRICED HIGH TO LOW</li><li>PRICED LOW TO HIGHT</li></ul></div>
    </aside>

    <main class="main">
      <h2 class="section-title">NEWEST ARRIVAL</h2>
      <div class="grid">
        <article class="card"><div class="card-photo p1" role="img" aria-label="Navy lace teddy product photo"><span class="sizes">SIZES: 34B, 34C, 32C,36B</span></div><div class="card-body"><div class="card-row"><span class="card-name">Teddy</span><span class="stars">★★★★☆</span></div><div class="price-row"><span class="price">$ 399.00</span><span class="dots">Avl : <i style="background:#2aa3a0"></i><i style="background:#a03a8a"></i><i style="background:#4a4a8a"></i></span></div><div class="actions"><span class="add">🛒 ADD TO CART</span><span>♥</span><span>⌕</span><span>⇄</span></div></div></article>
        <article class="card"><div class="card-photo p2" role="img" aria-label="Green bra and garter belt product photo"></div><div class="card-body"><div class="card-row"><span class="card-name">Bra, Garter Belt</span><span class="stars">★★★☆☆</span></div><div class="price">$ 399.00</div><div class="actions"><span class="add">🛒 ADD TO CART</span><span>♥</span><span>⌕</span><span>⇄</span></div></div></article>
        <article class="card"><div class="card-photo p3" role="img" aria-label="Black lace g-string set product photo"></div><div class="card-body"><div class="card-row"><span class="card-name">G-String</span><span class="stars">★★★★☆</span></div><div class="price">$ 399.00</div><div class="actions"><span class="add">🛒 ADD TO CART</span><span>♥</span><span>⌕</span><span>⇄</span></div></div></article>
        <article class="card"><div class="card-photo p4" role="img" aria-label="Teal lace chemise product photo"></div><div class="card-body"><div class="card-row"><span class="card-name">Chemise</span><span class="stars">★★★★☆</span></div><div class="price">$ 399.00</div><div class="actions"><span class="add">🛒 ADD TO CART</span><span>♥</span><span>⌕</span><span>⇄</span></div></div></article>
        <article class="card"><div class="card-photo p5" role="img" aria-label="Red lace babydoll product photo"></div><div class="card-body"><div class="card-row"><span class="card-name">Bra, Garter Belt</span><span class="stars">★★★☆☆</span></div><div class="price">$ 399.00</div><div class="actions"><span class="add">🛒 ADD TO CART</span><span>♥</span><span>⌕</span><span>⇄</span></div></div></article>
        <article class="card"><div class="card-photo p6" role="img" aria-label="Black bustier product photo"></div><div class="card-body"><div class="card-row"><span class="card-name">G-String</span><span class="stars">★★★★☆</span></div><div class="price">$ 399.00</div><div class="actions"><span class="add">🛒 ADD TO CART</span><span>♥</span><span>⌕</span><span>⇄</span></div></div></article>
      </div>

      <h2 class="section-title">TOP SELLERS</h2>
      <div class="grid">
        <article class="card"><div class="card-photo p7" role="img" aria-label="Black lace teddy product photo"><span class="sizes">SIZES: 34B, 34C, 32C,36B</span></div><div class="card-body"><div class="card-row"><span class="card-name">Teddy</span><span class="stars">★★★★☆</span></div><div class="price-row"><span class="price">$ 399.00</span><span class="dots">Avl : <i style="background:#2aa3a0"></i><i style="background:#a03a8a"></i><i style="background:#4a4a8a"></i></span></div><div class="actions"><span class="add">🛒 ADD TO CART</span><span>♥</span><span>⌕</span><span>⇄</span></div></div></article>
        <article class="card"><div class="card-photo p8" role="img" aria-label="Plum bra and garter belt product photo"></div><div class="card-body"><div class="card-row"><span class="card-name">Bra, Garter Belt</span><span class="stars">★★★☆☆</span></div><div class="price">$ 399.00</div><div class="actions"><span class="add">🛒 ADD TO CART</span><span>♥</span><span>⌕</span><span>⇄</span></div></div></article>
        <article class="card"><div class="card-photo p9" role="img" aria-label="Black strappy g-string set product photo"></div><div class="card-body"><div class="card-row"><span class="card-name">G-String</span><span class="stars">★★★★☆</span></div><div class="price">$ 399.00</div><div class="actions"><span class="add">🛒 ADD TO CART</span><span>♥</span><span>⌕</span><span>⇄</span></div></div></article>
        <article class="card"><div class="card-photo p10" role="img" aria-label="Red lace off-shoulder chemise product photo"></div><div class="card-body"><div class="card-row"><span class="card-name">Chemise</span><span class="stars">★★★★☆</span></div><div class="price">$ 399.00</div><div class="actions"><span class="add">🛒 ADD TO CART</span><span>♥</span><span>⌕</span><span>⇄</span></div></div></article>
        <article class="card"><div class="card-photo p11" role="img" aria-label="Black lace long-sleeve dress product photo"></div><div class="card-body"><div class="card-row"><span class="card-name">Bra, Garter Belt</span><span class="stars">★★★☆☆</span></div><div class="price">$ 399.00</div><div class="actions"><span class="add">🛒 ADD TO CART</span><span>♥</span><span>⌕</span><span>⇄</span></div></div></article>
        <article class="card"><div class="card-photo p12" role="img" aria-label="Pink and black babydoll product photo"></div><div class="card-body"><div class="card-row"><span class="card-name">G-String</span><span class="stars">★★★★☆</span></div><div class="price">$ 399.00</div><div class="actions"><span class="add">🛒 ADD TO CART</span><span>♥</span><span>⌕</span><span>⇄</span></div></div></article>
      </div>

      <div class="pager"><span>«</span><span>1</span><span>2</span><span>3</span><span>4</span><span>5</span><span>6</span><span class="cur">7</span><span>8</span><span>9</span><span>»</span></div>
    </main>
  </div>
</div>

<section class="promo">
  <div class="wrap">
    <div><h2>GET UP TO <b>70%</b> OFF ON ALL PRODUCTS</h2><p>IT IS A LONG ESTABLISHED FACT THAT A READER WILL BE DISTRACTED BY THE READABLE CONTENT OF A PAGE WHEN LOOKING AT ITS LAYOUT.</p></div>
    <span class="btn">Shop now!</span>
  </div>
</section>

<footer class="footer">
  <div class="wrap">
    <div class="f-brand"><div class="logo"><span class="logo-name">PLUMLINE</span><span class="logo-sub">LINGERIE</span></div><p>It is a long established fact that a reader will be distracted by the readable content of a page when Lorem Ipsum is that it has</p><p style="margin-top:4px;color:#fff">Read more info »</p></div>
    <div class="f-col" style="width:128px"><h5>Information</h5><ul><li>My Account</li><li>Privacy Policy</li><li>Cart</li><li>Checkout</li><li>Shipping</li></ul></div>
    <div class="f-col" style="width:135px"><h5>Our Services</h5><ul><li>My Account</li><li>Privacy Policy</li><li>Cart</li><li>Checkout</li><li>Shipping</li></ul></div>
    <div class="f-col" style="width:138px"><h5>My Account</h5><ul><li>My Account</li><li>Privacy Policy</li><li>Cart</li><li>Checkout</li><li>Shipping</li></ul></div>
    <div class="f-col f-news"><h5>Newsletter</h5><p>Sign Up for Our Newsletter &amp; Promotion</p><input value="Enter Your email id"><br><span class="btn">Subscribe</span></div>
    <div class="f-col f-contact"><h5>Contact Us</h5><ul><li><b>ADDRESS :</b> # lorem ipsum<br>Dummy Text Lorem</li><li style="margin-top:14px"><b>PHONE :</b> (000)-121-1231</li><li><b>FAX :</b> (000)-121-1231</li><li><b>EMAIL :</b> info@plumline.example</li></ul></div>
  </div>
</footer>
<div class="base">
  <div class="wrap"><span>© Copy Rights 2016 Plumline. All Rights Reserved.</span><div class="social"><i></i><i></i><i></i><i></i><i></i></div></div>
</div>

</body>
</html>
```